Brochure/flyer for Cloth Nappy Company

My Business name is Willow Dapplez Nappies
I am wanting a A4 size brochure (Flyer) to be folded twice. Measurements when folded 210 x 99 mm
I am just about to launch my Modern Cloth Nappy Products and i am wanting a brochure to target new mum's who aren't familiar with Modern cloth nappies and also for mums who are familiar with modern cloth nappies but are looking at trying my brand.
I want the Brochure to be very informative but yet Simple to read. I want people to feel like they want to buy my nappies after they read my Brochure.
The Brochure can be reworded and additional information can be added if you feel its needed, But i would like all the information listed below to be on the brochure.

MOTO: Cloth Nappies The Modern Way

The nappy design is designed in Australia and Australian Owned.

WHY USE CLOTH?
-Save thousands of Dollars
-Easy to use
-Looks Cute
-Super Absorbency
It costs approximately $3000 to use disposable nappies on a child from birth until 2 and a half years, that is Approximately 6000 nappies going into Landfill. This is based on a child going through 6-8 nappies per day.
Modern cloth nappies, on the other hand, cost around $500 for a full stash of 24 nappies. This allows for the child to wear 6-8 nappies per day with a load of nappies going in the wash every 2-3 days. As we have a range of nappies that are one-size-fits-most for bubs ranging from 3kg to 18kg, that $500 would cover your complete stash from birth right through to toilet training, Not to mention the money you would save by using the nappies again for any subsequent Children you may have.
Eliminates your baby's exposure to harmful Chemicals that can be in disposable nappies.
The manufacturing and use of disposable nappies can amount to 2-3 times more wasted water than using cloth nappies
Using Disposable Nappies fill up our landfill, Disposable nappies take more than 100 years to decompose, possibly up to 500 years.

PRODUCTS AVAILABLE:
Newborn: All in One (AIO) Fits approx 2-7kg
Velcro All in Two, One size Fits Most (OSFM) fits approx 3 to 18kg
Snap All in Two, One size Fits Most (OSFM) Fits Approx 3 to 18kg
Extra Inserts
Wetbags
Bamboo Biodegradable liners

The Materials used and features:
All in 2 Nappy (AI2):
Outer Shell Features- A waterproof TPU shell to keep all the wetness in.
Lining is a made of Microfleece material which is soft on baby's skin and Wicks moisture away from the baby's skin it is also very fast drying
Double leg Gussets to avoids any potential side leg Leaks
a poo guard at the back to reduce any leaks from occurring up the back
Insert is Made from 70% Bamboo and 30% Organic Cotton, The extra trim insert with extra absorbency qualities that can easily be double up for a heavy wetting baby or for an all night solution.

Insert snaps in and out Which is easy to remove and replace
A Pocket opening is also available to add a Booster in for long naps or for night time use. Insert is 2 layers sewn together and then folded twice to create 6 layers of absorbency. Unsnap insert from shell for washing, As there is not 3 layers sewn together like most inserts, it dries much quicker and washes more thoroughly, therefore less chance of smells accumulating

Why are these inserts so great?
– Super soft and silky
– Very breathable
– Naturally Anti-bacterial
– Absorbs 3 to 4 times more than cotton
– Doesn't feel sticky or uncomfortable when wet

The newborn nappy has a TPU waterproof Shell and is a all in one (AIO), has 4 layers of absorbency of 70% Bamboo and 30% Organic Cotton, With Microfleece lining which is super soft on newborns delicate skin.
The newborn nappy has a snap to hold down the front of the nappy where the umbilical cord will be for the first week or so. there is also snaps to adjust the size that little bit smaller for Premature babies or small babies. There is also double leg gussets to avoid any leaks around the legs. There is also a Poo guard at the back to avoid any leaks coming up from the back. The waist has a cross over snap for a extra small waist

PRICING:
One Size Fits Most:
Velcro: $25.95
Snap: $25.95
All In One Newborn:
$19.95

PACKAGES:
Price Depends on What nappies you choose for your package

Trial 3 pack: 5% Discount
6 Pack: 10% Discount
12 Pack: 15% Discount
24 Pack: 20% discount

Extra Inserts $7.00
Wetbags: $10
Bamboo Biodegradable Liners: $10
Contact Details:
Lorna Whitcombe
Phone: 0437816204
E-mail: willowdapplezbubs@fernmail.example
Facebook: www.bubsbook.example/WillowDapplezBubs
Updates

I have changed a few things on the brief so please read carefully before changing or making another design,

Thanks :) 

Target Market(s)

Mums and Dads, care takers, Guardians and grandparents

Industry/Entity Type

Baby

Requirements
Must have
• Must have the Logo and picture i have sent but you are welcome to put other pictures of babies but please do not put pictures of babies with disposable nappies on. and if you are going to put pics of babies i would prefer the pictures not to show how the Velcro or snaps look at the front of the nappy. for example: put pictures that show the nappy side on or from the back. You could put pictures of babies or of nature etc "saving the Environment"
Should not have
• no pictures of other cloth nappy brands No disposable nappies

```html
<!DOCTYPE html>
<html lang="en">
<head>
<meta charset="utf-8">
<title>Why Use Cloth? – Inside Spread</title>
<link href="https://fonts.googleapis.com/css2?family=Cagliostro&family=Jost:wght@600&display=swap" rel="stylesheet">
<style>
  :root {
    --paper: #fbf9fc;
    --paper-tint: #f1e6f2;
    --ink: #4a4548;
    --rose: #c2307e;
    --rose-head: #a9347c;
    --plum: #8a3a92;
    --rule: #d88cb8;
    --box-fill: #fbe9f3;
    --box-line: #e6a7c9;
    --photo-a: #efe4d6;
    --photo-b: #e2cdb8;
  }
  * { box-sizing: border-box; margin: 0; padding: 0; }
  html, body { width: 1200px; height: 852px; overflow: hidden; }
  body {
    background: var(--paper);
    font-family: "Cagliostro", "Trebuchet MS", sans-serif;
    color: var(--ink);
  }
  .spread {
    position: relative;
    width: 1200px; height: 852px;
    background:
      radial-gradient(ellipse 260px 300px at 240px 380px, var(--paper-tint), transparent 70%),
      radial-gradient(ellipse 300px 340px at 610px 520px, var(--paper-tint), transparent 70%),
      radial-gradient(ellipse 240px 260px at 1040px 260px, var(--paper-tint), transparent 70%),
      linear-gradient(180deg, #fdfcfd 0%, var(--paper) 100%);
  }
  .fold {
    position: absolute; top: 0; width: 1px; height: 852px;
    background: var(--rule);
  }
  .fold--one { left: 405px; }
  .fold--two { left: 806px; }
  .panel { position: absolute; top: 0; }
  .panel--left { left: 46px; width: 330px; top: 42px; }
  .panel--middle { left: 446px; width: 340px; top: 40px; }
  .panel--right { left: 846px; width: 330px; top: 40px; }
  .heading {
    font-family: "Jost", "Futura", sans-serif;
    font-weight: 600;
    color: var(--rose-head);
    font-size: 23px;
    line-height: 30px;
  }
  .subheading {
    font-family: "Jost", "Futura", sans-serif;
    font-weight: 600;
    color: var(--plum);
    font-size: 16.5px;
    line-height: 24px;
    margin: 26px 0 9px;
  }
  .benefits {
    list-style: none;
    margin: 4px 0 14px -4px;
    width: 274px;
    padding: 6px 0 4px 24px;
    background: var(--box-fill);
    border: 1px solid var(--box-line);
    border-radius: 6px;
    font-size: 18px;
    line-height: 25.3px;
    color: var(--rose);
  }
  .benefits li::before { content: "•"; margin-right: 6px; }
  .copy { font-size: 15.4px; line-height: 25.3px; margin-bottom: 8px; white-space: nowrap; }
  .copy--tight { line-height: 22.8px; margin-bottom: 9px; }
  .copy--rose { color: var(--rose); }
  .copy--plum { color: var(--plum); }
  .products .heading { margin: 13px 0 9px; }
  .product-list { list-style: none; font-size: 15.4px; line-height: 25.3px; white-space: nowrap; }
  .baby-photo {
    position: absolute; left: 846px; top: 426px;
    width: 308px; height: 380px;
    border: 1.5px solid var(--box-line);
    border-radius: 10px;
    background: radial-gradient(ellipse at 50% 55%, var(--photo-b), var(--photo-a) 70%);
  }
</style>
</head>
<body>
<main class="spread">
  <div class="fold fold--one"></div>
  <div class="fold fold--two"></div>

  <section class="panel panel--left">
    <h2 class="heading">Why Use Cloth?</h2>
    <ul class="benefits">
      <li>Save thousands of Dollars</li>
      <li>Easy to use</li>
      <li>Looks Cute</li>
      <li>Super Absorbency</li>
    </ul>
    <p class="copy">It costs approximately $3000 to use<br>disposable nappies on a child from birth until<br>2 and a half years, that is approximately<br>6000 nappies going into Landfill. This is<br>based on a child going through 6-8 nappies<br>per day.</p>
    <p class="copy">Modern cloth nappies, on the other hand,<br>cost around $500 for a full stash of 24<br>nappies. This allows for the child to wear 6-8<br>nappies per day with a load of nappies going<br>in the wash every 2-3 days. As we have a<br>range of nappies that are one-size-fits-most<br>for bubs ranging from 3kg to 18kg, that $500<br>would cover your complete stash from birth<br>right through to toilet training, not to<br>mention the money you would save by using<br>the nappies again for any subsequent<br>children you may have.</p>
    <p class="copy copy--rose">Eliminates your baby's exposure to harmful<br>chemicals that can be in disposable nappies.</p>
    <p class="copy">The manufacturing and use of disposable<br>nappies can amount to 2-3 times more<br>wasted water than using cloth nappies.</p>
  </section>

  <section class="panel panel--middle">
    <p class="copy">Using Disposable Nappies fill up our landfill,<br>disposable nappies take more than 100 years<br>to decompose, possibly up to 500 years.</p>
    <div class="products">
      <h2 class="heading">Products Available:</h2>
      <ul class="product-list">
        <li>Newborn: All in One (AIO) Fits approx 2-7kg</li>
        <li>Velcro All in Two, One size Fits Most (OSFM)<br>fits approx 3 to 18kg</li>
        <li>Snap All in Two, One size Fits Most (OSFM)<br>Fits Approx 3 to 18kg</li>
        <li>Extra Inserts</li>
        <li>Wetbags</li>
        <li>Bamboo Biodegradable liners</li>
      </ul>
    </div>
    <h3 class="subheading">The Materials used and features:</h3>
    <p class="copy copy--tight">All in 2 Nappy (AI2):</p>
    <p class="copy copy--tight">Outer Shell Features- A waterproof TPU shell<br>to keep all the wetness in.</p>
    <p class="copy copy--tight">Lining is made of Microfleece material which<br>is soft on baby's skin and Wicks moisture<br>away from the baby's skin, it is also very fast<br>drying</p>
    <p class="copy copy--tight">Double leg gussets to avoid any potential<br>side leg Leaks</p>
    <p class="copy copy--tight">A poo guard at the back to reduce any leaks<br>from occurring up the back</p>
    <p class="copy copy--plum">Insert is Made from 70% Bamboo and 30%<br>Organic Cotton, The extra trim insert with<br>extra absorbency qualities that can easily be</p>
  </section>

  <section class="panel panel--right">
    <p class="copy copy--plum">doubled up for a heavy wetting baby or for an<br>all night solution.</p>
    <p class="copy">Insert snaps in and out Which is easy to<br>remove and replace</p>
    <p class="copy">A Pocket opening is also available to add a<br>Booster in for long naps or for night time use.<br>Insert is 2 layers sewn together and then<br>folded twice to create 6 layers of absorbency.<br>Unsnap insert from shell for washing, As<br>there is not 3 layers sewn together like most<br>inserts, it dries much quicker and washes<br>more thoroughly, therefore less chance of<br>smells accumulating.</p>
  </section>

  <div class="baby-photo" role="img" aria-label="Photo of a baby in a cream cloth nappy lying on a soft woolly rug, holding its feet"></div>
</main>
</body>
</html>
```